Clinical Hypnotherapist needs business card design

I need a business card design that gives the impression of being approachable yet professional. As a clinical hypnotherapist I need to create trust from my clients to allow me access to their inner mind to enable them to make changes and to start to live the life that they want to live. My website is www.serenvale.com.au and I would like my business cards to reflect my website. I would like a space for appointment details on the back of the card.

```html
<!DOCTYPE html>
<html lang="en">
<head>
<meta charset="utf-8">
<title>Clara Whitford – Clinical Hypnotherapist</title>
<link rel="stylesheet" href="https://fonts.googleapis.com/css2?family=Tinos&family=Marcellus+SC&display=swap">
<style>
  :root {
    --magenta: #cc26b1;
    --magenta-soft: #d64fbf;
    --mist-light: #e6eaea;
    --mist-mid: #cfd6d6;
    --mist-edge: #b7bfc0;
    --white: #ffffff;
    --monogram: #d6a9d3;
  }
  * { margin: 0; padding: 0; box-sizing: border-box; }
  html, body { width: 1200px; height: 653px; overflow: hidden; background: #ffffff; }
  .card {
    position: relative;
    width: 1200px;
    height: 653px;
    overflow: hidden;
    background: radial-gradient(ellipse at 60% 45%, var(--mist-light) 0%, var(--mist-mid) 55%, var(--mist-edge) 100%);
  }
  .card__shapes { position: absolute; inset: 0; }
  .monogram {
    position: absolute;
    left: 800px;
    top: 118px;
    font-family: "Tinos", serif;
    font-size: 230px;
    line-height: 1;
    color: var(--monogram);
    letter-spacing: -4px;
  }
  .identity { position: absolute; right: 56px; top: 32px; text-align: left; }
  .identity__name {
    font-family: "Tinos", serif;
    font-weight: 400;
    font-size: 58px;
    line-height: 1;
    color: var(--magenta);
    margin-left: 78px;
  }
  .identity__role {
    font-family: "Marcellus SC", serif;
    font-size: 23px;
    letter-spacing: 3.5px;
    color: var(--magenta);
    margin-top: 16px;
  }
  .contact {
    position: absolute;
    left: 46px;
    top: 480px;
    list-style: none;
    font-family: "Marcellus SC", serif;
    font-size: 27px;
    letter-spacing: 3.5px;
    color: var(--white);
    line-height: 42px;
  }
</style>
</head>
<body>
<div class="card">
  <svg class="card__shapes" width="1200" height="653" viewBox="0 0 1200 653">
    <defs>
      <radialGradient id="ornamentTone" cx="50%" cy="50%" r="55%">
        <stop offset="0%" stop-color="#cc26b1"/>
        <stop offset="70%" stop-color="#cc26b1" stop-opacity="0.85"/>
        <stop offset="100%" stop-color="#cc26b1" stop-opacity="0"/>
      </radialGradient>
    </defs>
    <path class="wave-highlight" fill="#ffffff"
          d="M470 352 C620 430 900 458 1200 436 L1200 474 C880 478 620 455 470 375 Z"/>
    <path class="wave-band" fill="#cc26b1"
          d="M0 37 L445 340 C600 440 880 478 1200 472 L1200 653 L0 653 Z"/>
    <g role="img" aria-label="Decorative magenta swirl ornament">
      <ellipse cx="345" cy="190" rx="240" ry="160" fill="url(#ornamentTone)"/>
    </g>
  </svg>

  <div class="monogram" aria-hidden="true">CW</div>

  <header class="identity">
    <h1 class="identity__name">Clara Whitford</h1>
    <p class="identity__role">Clinical Hypnotherapist</p>
  </header>

  <ul class="contact">
    <li>Website: www.serenvale.com.au</li>
    <li>Email: clara@serenvale.com.au</li>
    <li>Tel: 0400 315 862</li>
  </ul>
</div>
</body>
</html>
```